Event Poster - Tarawera Mist Fest 2018 (Need ASAP)

Create a poster for an upcoming vape event, located in Waikato, Hamilton, New Zealand.

Mist Fest is an event where lots of shops come to a location, and the public are welcomed and they all vape, buy vape products, socialize, drink beer and have fun.

VISIT THE EVENT WEBSITE FOR INFO - www.taraweramistfest.co.nz

We have created a website at, as you can see the logo and design is a bit boring and plain, so we dont really want it to look anything like that, The logo that is created to suit the poster will be able to be

Need a poster done up so we can send it around, post it up on boards, share on social media etc

I have attached previous events from nearby towns, for reference, but I want something much better.

Target Market(s)

25-45 Male / Female

Requirements
Must have
• - Tarawera Mist Fest 2018
• - Saturday, 2nd June 2018
• - 12-10pm
• - R18 Event (important for public to know)
• - Vendors, Prizes, Comps, Cloud Liquid Medals, Entertainment, Giveaways & More
• - The Corner Alehouse (14 Moller Ln, Kopuku, Hamilton)
• - mention something along lines "Join Tarawera's Opening Mist Fest"
• - "Grab Your Passes at www.taraweramistfest.co.nz NOW"
• - I want people to know they can buy it from a store as well "The Haze Hut"
Nice to have
• Our City colors are Red,Yellow,Black which is symbolic for "Waikato" so it would be nice to have those integrated in there. Alot of the other Mist Fest events have dark, bogan, amateur look done to them, so I want ours to be just a much better version.
• To Clarify, Hamilton is a city inside the Waikato
• I might want to put sponsors on there as well, possibly 10-20, but maybe only a few if space is a problem

```html
<!DOCTYPE html>
<html lang="en">
<head>
<meta charset="utf-8">
<title>Tarawera Mist Fest 2018</title>
<link href="https://fonts.googleapis.com/css2?family=Montserrat:wght@300;400;600;700;800;900&display=swap" rel="stylesheet">
<style>
  :root {
    --black: #0b0507;
    --red: #e0151c;
    --yellow: #f5d21a;
    --lime: #d6e618;
    --white: #ffffff;
  }
  * { margin: 0; padding: 0; box-sizing: border-box; }
  html, body { width: 920px; height: 1200px; overflow: hidden; background: var(--black); }
  body { font-family: "Montserrat", sans-serif; color: var(--white); }
  .poster { position: relative; width: 920px; height: 1200px; overflow: hidden; }
  .backdrop {
    position: absolute; inset: 0;
    background:
      radial-gradient(ellipse 420px 320px at 640px 240px, rgba(201,169,180,.55), transparent 70%),
      radial-gradient(ellipse 380px 300px at 260px 420px, rgba(160,20,40,.75), transparent 75%),
      radial-gradient(ellipse 300px 220px at 300px 900px, rgba(200,20,30,.45), transparent 75%),
      linear-gradient(180deg, #6a1020 0%, #3c0812 45%, #1a0508 75%, var(--black) 100%);
  }
  .line { position: absolute; line-height: 1; white-space: nowrap; }
  .right { right: 34px; text-align: right; }

  .rating { left: 540px; width: 230px; top: 30px; text-align: center; font-size: 72px; font-weight: 900; color: var(--red); letter-spacing: -2px; }
  .rating-label { left: 540px; width: 230px; top: 104px; text-align: center; font-size: 25px; font-weight: 400; letter-spacing: 7px; color: var(--black); }

  .title-region { top: 138px; font-size: 80px; font-weight: 400; color: var(--white); -webkit-text-stroke: 2px var(--black); letter-spacing: -1px; }
  .title-main { top: 223px; font-size: 230px; font-weight: 700; letter-spacing: -8px; }
  .title-sub { top: 425px; font-size: 170px; font-weight: 600; letter-spacing: -4px; }
  .title-year { top: 566px; font-size: 108px; font-weight: 700; color: var(--lime); letter-spacing: -2px; }

  .weekday { top: 682px; font-size: 42px; font-weight: 300; }
  .date { top: 712px; font-size: 96px; font-weight: 600; letter-spacing: -2px; }
  .month { top: 791px; font-size: 80px; font-weight: 800; color: var(--yellow); }
  .hours { top: 863px; font-size: 26px; font-weight: 800; color: var(--red); display: flex; align-items: center; gap: 6px; }

  .venue-name { top: 893px; font-size: 26px; font-weight: 800; color: var(--yellow); display: flex; align-items: center; gap: 8px; }
  .venue-address { top: 924px; font-size: 15px; font-weight: 500; }

  .divider { position: absolute; left: 0; top: 0; }

  .features { position: absolute; right: 34px; top: 978px; text-align: right; font-size: 19px; font-weight: 800; letter-spacing: 1.5px; line-height: 25px; }
  .red { color: var(--red); }
  .yellow { color: var(--yellow); }

  .invite-lead { left: 38px; top: 931px; font-size: 40px; font-weight: 400; color: var(--yellow); }
  .invite-place { left: 36px; top: 964px; font-size: 56px; font-weight: 800; }
  .invite-tail { left: 38px; top: 1026px; font-size: 36px; font-weight: 300; }
  .invite-tail .yellow { font-weight: 400; }
  .invite-tail strong { font-weight: 800; }

  .brand { position: absolute; display: flex; align-items: center; gap: 8px; font-size: 15px; font-weight: 800; line-height: 1.1; color: var(--white); }
  .brand-event { left: 40px; top: 1116px; }
  .brand-square { width: 34px; height: 34px; background: var(--yellow); flex: none; }
  .brand-store { left: 196px; top: 1124px; font-size: 20px; }

  .tickets-prompt { left: 436px; top: 1108px; font-size: 21px; font-weight: 400; }
  .tickets-band { position: absolute; left: 415px; top: 1139px; width: 505px; height: 31px; background: var(--yellow); display: flex; align-items: center; padding-left: 22px; gap: 10px; color: var(--black); font-size: 19px; font-weight: 800; white-space: nowrap; }
  .tickets-band .now { color: var(--red); font-size: 24px; font-weight: 900; }
</style>
</head>
<body>
<main class="poster">
  <div class="backdrop" role="img" aria-label="Moody red photograph of a person in a cap and track jacket exhaling a cloud of vapour, with lit e-liquid bottles in the lower left"></div>

  <div class="line rating">R18</div>
  <div class="line rating-label">EVENT</div>

  <div class="line right title-region">TARAWERA</div>
  <div class="line right title-main">MIST</div>
  <div class="line right title-sub">FEST</div>
  <div class="line right title-year">2018</div>

  <div class="line right weekday">SATURDAY</div>
  <div class="line right date">2ND</div>
  <div class="line right month">JUNE</div>
  <div class="line right hours">
    <svg width="18" height="18" viewBox="0 0 16 16" aria-hidden="true"><circle cx="8" cy="8" r="6.5" fill="none" stroke="#fff" stroke-width="1.6"/><path d="M8 4v4h3" fill="none" stroke="#fff" stroke-width="1.6"/></svg>
    12-10PM
  </div>

  <div class="line right venue-name">
    <svg width="16" height="22" viewBox="0 0 16 22" aria-hidden="true"><path d="M8 0a8 8 0 0 1 8 8c0 6-8 14-8 14S0 14 0 8a8 8 0 0 1 8-8z" fill="#e0151c"/><circle cx="8" cy="8" r="3" fill="#0b0507"/></svg>
    THE CORNER ALEHOUSE
  </div>
  <div class="line right venue-address">14 MOLLER LN, KOPUKU, HAMILTON</div>

  <svg class="divider" width="920" height="1200" aria-hidden="true">
    <polyline points="888,958 540,958 490,1050 462,1050" fill="none" stroke="#f5d21a" stroke-width="1.3"/>
  </svg>

  <div class="features">
    <div>VENDORS, PRIZES, <span class="red">COMPS,</span></div>
    <div class="red">CLOUD LIQUID MEDALS,</div>
    <div class="yellow">ENTERTAINMENT,</div>
    <div>GIVEAWAYS &amp; MORE</div>
  </div>

  <div class="line invite-lead">JOIN</div>
  <div class="line invite-place">TARAWERA'S</div>
  <div class="line invite-tail"><span class="yellow">OPENING</span> <strong>MIST</strong> FEST</div>

  <div class="brand brand-event"><span class="brand-square"></span><span>TARAWERA<br>MIST FEST</span></div>
  <div class="brand brand-store">THE HAZE HUT</div>

  <div class="line tickets-prompt">Grab Your Passes at</div>
  <div class="tickets-band">www.taraweramistfest.co.nz <span class="now">NOW</span></div>
</main>
</body>
</html>
```